New Coffee Shop business card

We are opening our new coffee shop and are needing business cards to take with us on February 6th to Atlanta, Ga to a show.

We will be offering the following menu type items:

coffee
teas
espresso
frappes
smoothies

sandwiches
soups
salads
pastries
ice cream

Our shop is in a rural country-side area and we would like to convey that feel in our shop. In addition to the cafe we will also be selling gifts and furniture and other home decor. Much of this merchandise will be rescued, refurbished or repurposed which is also a core value of what we are all about.

We have a company logo we would like incorporated into the design.

We will also provide files that have the elements of the logo which may also be useful in the design of the card.

Since we are not open yet we need one slightly altered version of the card as well as the final product which states "Opening in the summer 2015"

Target Market(s)

moderate to slightly upscale and folksy.

Industry/Entity Type

Coffee Shop

Contact Information for Business Card

Fern Hollow Coffee
name
address
phone number
email

Card

Font styles to use
Sans Serif

Requirements
Must have
• Must include Logo
• Must include information on menu.
• Must include information on our merchandise sales as described inthe project description.
• Color scheme to complement the logo
Nice to have
• The following descriptions
• "We are also selling gifts, furniture, and other home decoration."
• "We rescue, refurbish, and repurpose old furniture so it can live again."

```html
<!DOCTYPE html>
<html lang="en">
<head>
<meta charset="utf-8">
<title>Fern Hollow Coffee – Business Cards</title>
<link rel="stylesheet" href="https://fonts.googleapis.com/css2?family=Crimson+Text:wght@400&display=swap">
<style>
  :root {
    --backdrop: #e4e4e2;
    --ink: #1f1f1f;
    --ink-soft: #2b2b2b;
    --paper-veil: rgba(255, 255, 255, 0.72);
    --paper-veil-soft: rgba(255, 255, 255, 0.55);
    --logo-light: #ffffff;
    --logo-dark: #1c1c1c;
    --card-shadow: 0 14px 30px rgba(0, 0, 0, 0.25);
  }
  * { box-sizing: border-box; margin: 0; padding: 0; }
  html, body {
    width: 1200px;
    height: 1000px;
    overflow: hidden;
    background: var(--backdrop);
    font-family: "Crimson Text", Georgia, serif;
    color: var(--ink);
  }
  .sheet {
    position: relative;
    width: 1200px;
    height: 1000px;
  }
  .card {
    position: absolute;
    left: 250px;
    width: 700px;
    height: 400px;
    overflow: hidden;
    box-shadow: var(--card-shadow);
    background: #fff;
  }
  .card--contact { top: 60px; }
  .card--menu { top: 530px; }

  .card__photo {
    position: absolute;
    inset: 0;
  }
  .card--contact .card__photo {
    background:
      linear-gradient(180deg, rgba(0,0,0,0) 55%, rgba(235,235,235,0.9) 100%),
      linear-gradient(100deg, #c9c9c9 0%, #8a8580 22%, #6b4a30 45%, #8a5a34 60%, #b9b6b2 80%, #e8e8e8 100%);
  }
  .card--menu .card__photo {
    background:
      radial-gradient(ellipse 22% 40% at 63% 58%, #2f3440 0%, #454a55 55%, rgba(80,84,92,0) 100%),
      linear-gradient(110deg, #e9e9e9 0%, #cfcfcf 40%, #9a9a9a 60%, #d8d8d8 85%, #c2c2c2 100%);
  }

  .veil {
    position: absolute;
    background: var(--paper-veil);
  }
  .card--contact .veil {
    left: 0; top: 160px; width: 700px; height: 240px;
    background: linear-gradient(180deg, var(--paper-veil-soft), var(--paper-veil));
  }
  .card--menu .veil {
    left: 0; top: 0; width: 400px; height: 400px;
  }

  .contact-block {
    position: absolute;
    left: 70px;
    top: 185px;
    font-size: 24px;
    line-height: 1.45;
    color: var(--ink-soft);
  }

  .menu-block {
    position: absolute;
    left: 55px;
    top: 28px;
    font-size: 21px;
    line-height: 1.2;
    color: var(--ink-soft);
  }
  .menu-block__title { margin-bottom: 14px; }
  .menu-block__columns {
    display: flex;
    gap: 70px;
  }
  .menu-block__list { list-style: none; }
  .menu-block__list--food { padding-top: 28px; }
  .menu-block__note {
    margin-top: 30px;
    font-size: 22px;
  }
  .menu-block__opening {
    margin-top: 22px;
    font-size: 22px;
  }

  .brand {
    position: absolute;
    display: flex;
    align-items: center;
    gap: 8px;
    font-size: 20px;
    line-height: 1;
    white-space: nowrap;
  }
  .brand__dot {
    width: 12px;
    height: 12px;
    border-radius: 50%;
    background: currentColor;
  }
  .card--contact .brand {
    right: 28px;
    top: 40px;
    color: var(--logo-light);
  }
  .card--menu .brand {
    right: 40px;
    bottom: 40px;
    color: var(--logo-dark);
  }
</style>
</head>
<body>
<main class="sheet">

  <section class="card card--contact">
    <div class="card__photo" role="img" aria-label="Close-up photograph of an espresso machine portafilter pouring into a cup"></div>
    <div class="veil"></div>
    <div class="brand"><span class="brand__dot"></span><span class="brand__name">Fern Hollow Coffee</span></div>
    <div class="contact-block">
      <p class="contact-block__name">Your Name Your Name</p>
      <p class="contact-block__address">Address, Country, State, Zip 000000</p>
      <p class="contact-block__phone">000 0000 0000</p>
      <p class="contact-block__email">your_email@company.com</p>
    </div>
  </section>

  <section class="card card--menu">
    <div class="card__photo" role="img" aria-label="Black and white photograph of a coffee mug on a table"></div>
    <div class="veil"></div>
    <div class="menu-block">
      <p class="menu-block__title">Menu:</p>
      <div class="menu-block__columns">
        <ul class="menu-block__list menu-block__list--drinks">
          <li>Coffee</li>
          <li>Teas</li>
          <li>Espresso</li>
          <li>Frappes</li>
          <li>Smoothies</li>
        </ul>
        <ul class="menu-block__list menu-block__list--food">
          <li>Sandwiches</li>
          <li>Soups</li>
          <li>Salads</li>
          <li>Pastries</li>
          <li>Ice cream</li>
        </ul>
      </div>
      <p class="menu-block__note">Gifts, furniture and other home deco.</p>
      <p class="menu-block__opening">Opening in the summer 2015.</p>
    </div>
    <div class="brand"><span class="brand__dot"></span><span class="brand__name">Fern Hollow Coffee</span></div>
  </section>

</main>
</body>
</html>
```